Edgy rebranded biz cards QBL

We are rebranding our 20 yr old mortgage company with a new logo and would like cards to compliment our new look.

Target Market(s)

potential home buyers or clients for refinance

Industry/Entity Type

Mortgage Brokerage

Contact Information for Business Card

418 W. Tamsin Rd #340
Henderson, NV 89152
702.481.5927 o
702-481-5920 f
www.quarrybluelend,com
nmls 612084
QBL is an equal housing lender

Font styles to use
Sans Serif

Colors
0455a3
3176b5
0393ce
33a6d7

Requirements
Must have
• space for a photo
Nice to have
• One side with the company info and the other with the person's info

```html
<!DOCTYPE html>
<html lang="en">
<head>
<meta charset="utf-8">
<title>Quarry Blue Lending – Business Card</title>
<link rel="stylesheet" href="https://fonts.googleapis.com/css2?family=Poppins:wght@400;500;600&family=Roboto:ital,wght@1,400&display=swap">
<style>
  :root{
    --brand-blue:#1672c0;
    --deep-blue:#0455a3;
    --slate:#6d7d92;
    --ring-grey:#8a8d92;
    --text-dark:#1d1d1f;
    --text-grey:#7b7f85;
    --card-white:#ffffff;
    --page-bg:#e9e7e3;
  }
  *{margin:0;padding:0;box-sizing:border-box;}
  html,body{width:900px;height:1200px;overflow:hidden;}
  body{background:var(--page-bg);font-family:"Poppins",Arial,sans-serif;position:relative;}

  .card{position:absolute;left:82px;width:738px;height:432px;border-radius:30px;overflow:hidden;
        box-shadow:0 6px 16px rgba(0,0,0,.25);}
  .card--front{top:137px;background:var(--card-white);}
  .card--back{top:640px;background:linear-gradient(90deg,#1a74c0 0%,#4f7fb0 45%,#6f7f94 100%);}

  .front-bands{position:absolute;inset:0;}

  .portrait{position:absolute;left:60px;top:34px;width:240px;height:240px;border-radius:50%;
            border:9px solid var(--ring-grey);background:var(--card-white);padding:4px;}
  .portrait__photo{width:100%;height:100%;border-radius:50%;
            background:radial-gradient(circle at 50% 40%,#f3f3f3 0%,#d9d9db 55%,#7c7e83 100%);}

  .brand{position:absolute;left:390px;top:120px;width:310px;text-align:center;color:var(--brand-blue);
         font-weight:600;line-height:1;}
  .brand__main{font-size:41px;letter-spacing:.5px;}
  .brand__sub{font-size:17px;letter-spacing:1px;margin-top:8px;}

  .person{position:absolute;left:45px;top:292px;}
  .person__name{font-size:21px;font-weight:600;color:var(--text-dark);}
  .person__title{font-size:15px;font-weight:400;color:var(--brand-blue);}
  .person__title sup{font-size:10px;}
  .person__line{display:flex;align-items:center;gap:12px;font-size:18px;color:var(--text-dark);margin-top:6px;}
  .icon{width:18px;height:18px;fill:var(--brand-blue);flex:none;}

  .contact{position:absolute;right:42px;top:252px;text-align:right;font-size:16px;color:var(--text-dark);}
  .contact__line{display:flex;justify-content:flex-end;align-items:center;gap:8px;height:25px;}
  .contact__line--plain{padding-right:26px;}

  .footer-rule{position:absolute;left:0;top:406px;width:580px;height:5px;background:var(--brand-blue);}
  .nmls{position:absolute;right:42px;top:398px;font-size:14px;font-weight:500;color:var(--text-grey);}

  .back-brand{position:absolute;left:0;right:0;top:160px;text-align:center;color:#fff;font-weight:600;line-height:1;}
  .back-brand__main{font-size:41px;letter-spacing:.5px;}
  .back-brand__sub{font-size:17px;letter-spacing:1px;margin-top:8px;}
  .tagline{position:absolute;left:0;right:0;top:346px;text-align:center;color:#fff;
           font-family:"Roboto",Arial,sans-serif;font-style:italic;font-size:16px;}
</style>
</head>
<body>

<section class="card card--front">
  <svg class="front-bands" width="738" height="432" viewBox="0 0 738 432" aria-hidden="true">
    <defs>
      <linearGradient id="band" x1="0" y1="0" x2="1" y2="0">
        <stop offset="0" stop-color="#6f7f94"/>
        <stop offset="1" stop-color="#1672c0"/>
      </linearGradient>
    </defs>
    <polygon points="0,0 300,0 0,210" fill="url(#band)"/>
    <polygon points="310,0 438,0 230,146 170,146" fill="url(#band)"/>
    <polygon points="0,260 90,200 110,230 0,300" fill="#7c8593"/>
  </svg>

  <div class="portrait"><div class="portrait__photo" role="img" aria-label="Portrait photo of the loan officer"></div></div>

  <div class="brand">
    <div class="brand__main">QUARRY BLUE</div>
    <div class="brand__sub">LENDING</div>
  </div>

  <div class="person">
    <div><span class="person__name">Ethan Marlow</span> <span class="person__title">Realtor<sup>®</sup></span></div>
    <div class="person__line">
      <svg class="icon" viewBox="0 0 18 18"><path d="M4 0h10a2 2 0 0 1 2 2v14a2 2 0 0 1-2 2H4a2 2 0 0 1-2-2V2a2 2 0 0 1 2-2zm0 3v11h10V3zm4 12.5v1h2v-1z"/></svg>
      5678-5678-567
    </div>
    <div class="person__line">
      <svg class="icon" viewBox="0 0 18 18"><path d="M1 4h16v11H1zm1.5 1.2 6.5 5 6.5-5z"/></svg>
      ethan@quarrybluelend.com
    </div>
  </div>

  <div class="contact">
    <div class="contact__line">702-481-5927
      <svg class="icon" viewBox="0 0 18 18"><path d="M2 6c0-2 3-3 7-3s7 1 7 3v2h-4V6.5H6V8H2zm2 3h10l2 6H2zm5 1.5a2 2 0 1 0 0 4 2 2 0 0 0 0-4z"/></svg></div>
    <div class="contact__line">702-481-5920
      <svg class="icon" viewBox="0 0 18 18"><path d="M5 1h8v4H5zM2 6h14v7h-3v4H5v-4H2zm4 5v4h6v-4z"/></svg></div>
    <div class="contact__line">www.quarrybluelend,com
      <svg class="icon" viewBox="0 0 18 18"><path d="M9 1a8 8 0 1 0 0 16A8 8 0 0 0 9 1zm0 1.6c.8.9 1.5 2.3 1.8 4.2H7.2C7.5 4.9 8.2 3.5 9 2.6zM2.7 8.4h3a12 12 0 0 0 0 1.2h-3zm9.6 0h3v1.2h-3a12 12 0 0 0 0-1.2zM7.1 8.4h3.8v1.2H7.1zm.1 2.8h3.6c-.3 1.9-1 3.3-1.8 4.2-.8-.9-1.5-2.3-1.8-4.2z"/></svg></div>
    <div class="contact__line">418 W. Tamsin Rd #340
      <svg class="icon" viewBox="0 0 18 18"><path d="M9 0a6 6 0 0 0-6 6c0 4.5 6 12 6 12s6-7.5 6-12a6 6 0 0 0-6-6zm0 3.5a2.5 2.5 0 1 1 0 5 2.5 2.5 0 0 1 0-5z"/></svg></div>
    <div class="contact__line contact__line--plain">Henderson, NV 89152</div>
  </div>

  <div class="footer-rule"></div>
  <div class="nmls">Nmls 612084</div>
</section>

<section class="card card--back">
  <div class="back-brand">
    <div class="back-brand__main">QUARRY BLUE</div>
    <div class="back-brand__sub">LENDING</div>
  </div>
  <p class="tagline">QBL is an equal housing lender</p>
</section>

</body>
</html>
```